Magazine Ad for Oil and Gas company
Advertisement for oil and gas event
Magazine Ad for Oil and Gas company  - Energy
Creative Brief
Energy
Oil and Gas, energy, Professionals
oil and gas, illustration
karnuvel karnuvel
Please find the attached sample of the AD that we are looking for. We want something more creative for the advertisement. The numbers that we need to reflect are in the info file. Please put a demo logo for oil and gas company like a drop. we dont need a logo we need the design of the AD in A4 Size format illustrator

```html
<!DOCTYPE html>
<html lang="en">
<head>
<meta charset="utf-8">
<title>Oil &amp; Gas Exhibition Flyer</title>
<link href="https://fonts.googleapis.com/css2?family=Oswald:wght@400;600;700&family=Roboto:wght@400;500;700&display=swap" rel="stylesheet">
<style>
  :root{
    --backdrop:#b9b9bd;
    --gold:#a88d63;
    --gold-dark:#8c7350;
    --ink:#1b1b1b;
    --paper:#ffffff;
    --panel:#ececec;
    --stripe:#e2e2e2;
    --muted:#6d6d6d;
  }
  *{box-sizing:border-box;margin:0;padding:0}
  html,body{width:1200px;height:901px;overflow:hidden}
  body{background:var(--backdrop);font-family:'Roboto',sans-serif;color:var(--ink);position:relative}
  .flyer{position:absolute;left:300px;top:25px;width:600px;height:850px;background:var(--paper);display:flex;flex-direction:column;box-shadow:0 6px 18px rgba(0,0,0,.25)}

  /* header */
  .masthead{height:100px;display:flex}
  .brand{flex:1;display:flex;align-items:center;gap:12px;padding-left:22px}
  .brand-mark{width:44px;height:44px;border-radius:50%;background:var(--ink)}
  .brand-name{font-family:'Oswald',sans-serif;font-weight:700;font-size:34px;line-height:1;color:var(--ink)}
  .brand-tagline{font-size:11px;color:var(--muted);margin-top:4px}
  .event-date{width:300px;background:var(--gold);color:var(--paper);display:flex;flex-direction:column;justify-content:center;padding-left:28px}
  .event-date .dates{font-family:'Oswald',sans-serif;font-weight:700;font-size:36px;line-height:1}
  .event-date .venue{font-family:'Oswald',sans-serif;font-size:15px;margin-top:6px;letter-spacing:.3px}

  /* headline */
  .headline{height:96px;background:var(--ink);color:var(--paper);display:flex;align-items:center;justify-content:center;text-align:center;font-family:'Oswald',sans-serif;font-weight:700;font-size:29px;line-height:1.12;letter-spacing:.5px;padding:0 30px}

  /* stats */
  .stats{height:300px;background:repeating-linear-gradient(135deg,var(--panel) 0 14px,var(--stripe) 14px 28px);display:grid;grid-template-columns:1fr 1fr;grid-template-rows:repeat(5,1fr);grid-auto-flow:column;padding:10px 0 12px}
  .why-tab{align-self:center;background:var(--gold);color:var(--ink);font-family:'Oswald',sans-serif;font-weight:700;font-size:24px;padding:6px 20px;width:240px;clip-path:polygon(0 0,100% 0,92% 100%,0 100%)}
  .stat{display:flex;align-items:center;gap:12px;padding-left:22px}
  .stat-icon{width:46px;height:32px;background:var(--gold);clip-path:polygon(18% 0,100% 0,82% 100%,0 100%);display:flex;align-items:center;justify-content:center;flex:none}
  .stat-number{font-family:'Oswald',sans-serif;font-weight:700;font-size:24px;line-height:1}
  .stat-label{font-size:10px;color:var(--muted);margin-top:2px}

  /* platform */
  .platform{height:150px;background:var(--ink);color:var(--paper);padding:18px 26px 0}
  .platform h2{font-family:'Oswald',sans-serif;font-weight:700;font-size:25px;letter-spacing:.4px;margin-bottom:14px}
  .benefits{list-style:none;display:grid;grid-template-columns:150px 170px 1fr;row-gap:9px;font-size:12px}
  .benefits li{display:flex;align-items:center;gap:7px}

  /* contact */
  .contact{height:44px;background:var(--gold);color:var(--paper);display:flex;align-items:center;justify-content:flex-end;gap:34px;padding-right:24px;font-size:11px}
  .contact-col{display:flex;flex-direction:column;gap:4px}
  .contact-col span{display:flex;align-items:center;gap:6px}

  /* confirm + sponsors */
  .confirm{height:30px;background:var(--ink);color:var(--paper);font-family:'Oswald',sans-serif;font-weight:600;font-size:15px;letter-spacing:.6px;display:flex;align-items:center;padding-left:26px}
  .sponsors{flex:1;display:grid;grid-template-columns:repeat(8,1fr);gap:8px;padding:14px 18px}
  .sponsor-group{display:flex;flex-direction:column;align-items:center;gap:8px}
  .sponsor-group h3{width:100%;background:var(--ink);color:var(--paper);font-size:8px;font-weight:500;text-align:center;padding:3px 0}
  .badge{width:22px;height:22px;border-radius:50%;background:#d7d7d7}
  .badge.alt{background:#c4d3c2}
</style>
</head>
<body>
<main class="flyer">
  <header class="masthead">
    <div class="brand">
      <span class="brand-mark"></span>
      <div>
        <div class="brand-name">karnuvel</div>
        <div class="brand-tagline">Your tagline goes here</div>
      </div>
    </div>
    <div class="event-date">
      <div class="dates">3 - 5 MARCH 2019</div>
      <div class="venue">International Exhibition Center</div>
    </div>
  </header>

  <h1 class="headline">BOOK A STAND AT LARGEST OIL<br>&amp; GAS EXHIBITION &amp; CONFERENCE</h1>

  <section class="stats">
    <div class="why-tab">WHY CHOOSE US ?</div>
    <div class="stat"><span class="stat-icon"><svg width="12" height="16" viewBox="0 0 12 16"><path d="M6 0C6 0 0 7 0 10.5a6 6 0 0 0 12 0C12 7 6 0 6 0z" fill="#fff"/></svg></span><div><div class="stat-number">4500</div><div class="stat-label">Attendees from 80 Countries</div></div></div>
    <div class="stat"><span class="stat-icon"><svg width="12" height="16" viewBox="0 0 12 16"><path d="M6 0C6 0 0 7 0 10.5a6 6 0 0 0 12 0C12 7 6 0 6 0z" fill="#fff"/></svg></span><div><div class="stat-number">500+</div><div class="stat-label">Professionals Engaged in the Conference</div></div></div>
    <div class="stat"><span class="stat-icon"><svg width="12" height="16" viewBox="0 0 12 16"><path d="M6 0C6 0 0 7 0 10.5a6 6 0 0 0 12 0C12 7 6 0 6 0z" fill="#fff"/></svg></span><div><div class="stat-number">100+</div><div class="stat-label">Technical Papers Presented</div></div></div>
    <div class="stat"><span class="stat-icon"><svg width="12" height="16" viewBox="0 0 12 16"><path d="M6 0C6 0 0 7 0 10.5a6 6 0 0 0 12 0C12 7 6 0 6 0z" fill="#fff"/></svg></span><div><div class="stat-number">13+</div><div class="stat-label">Technical Sessions</div></div></div>

    <div class="stat"><span class="stat-icon"><svg width="12" height="16" viewBox="0 0 12 16"><path d="M6 0C6 0 0 7 0 10.5a6 6 0 0 0 12 0C12 7 6 0 6 0z" fill="#fff"/></svg></span><div><div class="stat-number">7750</div><div class="stat-label">Sqm Exhibition Space</div></div></div>
    <div class="stat"><span class="stat-icon"><svg width="12" height="16" viewBox="0 0 12 16"><path d="M6 0C6 0 0 7 0 10.5a6 6 0 0 0 12 0C12 7 6 0 6 0z" fill="#fff"/></svg></span><div><div class="stat-number">100+</div><div class="stat-label">Industry Leaders Participated</div></div></div>
    <div class="stat"><span class="stat-icon"><svg width="12" height="16" viewBox="0 0 12 16"><path d="M6 0C6 0 0 7 0 10.5a6 6 0 0 0 12 0C12 7 6 0 6 0z" fill="#fff"/></svg></span><div><div class="stat-number">56</div><div class="stat-label">Companies Exhibited</div></div></div>
    <div class="stat"><span class="stat-icon"><svg width="12" height="16" viewBox="0 0 12 16"><path d="M6 0C6 0 0 7 0 10.5a6 6 0 0 0 12 0C12 7 6 0 6 0z" fill="#fff"/></svg></span><div><div class="stat-number">5</div><div class="stat-label">Technical Panels</div></div></div>
    <div class="stat"><span class="stat-icon"><svg width="12" height="16" viewBox="0 0 12 16"><path d="M6 0C6 0 0 7 0 10.5a6 6 0 0 0 12 0C12 7 6 0 6 0z" fill="#fff"/></svg></span><div><div class="stat-number">1</div><div class="stat-label">Plenary Session</div></div></div>
  </section>

  <section class="platform">
    <h2>GAS &amp; OIL EVENT IS A PLATFORM FOR:</h2>
    <ul class="benefits">
      <li><svg width="11" height="9" viewBox="0 0 11 9"><path d="M1 4.5l3 3L10 1" stroke="#a88d63" stroke-width="2" fill="none"/></svg>Innovation</li>
      <li><svg width="11" height="9" viewBox="0 0 11 9"><path d="M1 4.5l3 3L10 1" stroke="#a88d63" stroke-width="2" fill="none"/></svg>Best Practices Sharing</li>
      <li><svg width="11" height="9" viewBox="0 0 11 9"><path d="M1 4.5l3 3L10 1" stroke="#a88d63" stroke-width="2" fill="none"/></svg>Technology Deployment Experiences</li>
      <li><svg width="11" height="9" viewBox="0 0 11 9"><path d="M1 4.5l3 3L10 1" stroke="#a88d63" stroke-width="2" fill="none"/></svg>Designed for Leaders</li>
      <li><svg width="11" height="9" viewBox="0 0 11 9"><path d="M1 4.5l3 3L10 1" stroke="#a88d63" stroke-width="2" fill="none"/></svg>E&amp;P Professionals</li>
      <li><svg width="11" height="9" viewBox="0 0 11 9"><path d="M1 4.5l3 3L10 1" stroke="#a88d63" stroke-width="2" fill="none"/></svg>Scientists Engaged in R&amp;D</li>
      <li><svg width="11" height="9" viewBox="0 0 11 9"><path d="M1 4.5l3 3L10 1" stroke="#a88d63" stroke-width="2" fill="none"/></svg>And, so much more!</li>
    </ul>
  </section>

  <section class="contact">
    <div class="contact-col">
      <span><svg width="11" height="8" viewBox="0 0 11 8"><rect x=".5" y=".5" width="10" height="7" fill="none" stroke="#fff"/><path d="M.5.5l5 4 5-4" fill="none" stroke="#fff"/></svg>info@karnuvel-events.com</span>
      <span><svg width="10" height="10" viewBox="0 0 10 10"><circle cx="5" cy="5" r="4.5" fill="none" stroke="#fff"/><path d="M.5 5h9M5 .5v9" stroke="#fff"/></svg>www.karnuvel-events.com</span>
    </div>
    <div class="contact-col">
      <span><svg width="10" height="10" viewBox="0 0 10 10"><path d="M2 0l2 2.5-1 1.5a6 6 0 0 0 3 3l1.5-1L10 8l-1.5 2C4 10 0 6 0 1.5z" fill="#fff"/></svg>(555) 014-2290</span>
      <span><svg width="10" height="10" viewBox="0 0 10 10"><path d="M2 0l2 2.5-1 1.5a6 6 0 0 0 3 3l1.5-1L10 8l-1.5 2C4 10 0 6 0 1.5z" fill="#fff"/></svg>(555) 014-2291</span>
    </div>
  </section>

  <div class="confirm">CONFIRM YOUR SPACE TODAY</div>

  <section class="sponsors">
    <div class="sponsor-group"><h3>Host</h3><span class="badge"></span><span class="badge alt"></span></div>
    <div class="sponsor-group"><h3>Organiser</h3><span class="badge alt"></span><span class="badge"></span></div>
    <div class="sponsor-group"><h3>Platinum</h3><span class="badge"></span><span class="badge alt"></span></div>
    <div class="sponsor-group"><h3>Gold</h3><span class="badge alt"></span><span class="badge"></span></div>
    <div class="sponsor-group"><h3>Silver</h3><span class="badge"></span><span class="badge alt"></span></div>
    <div class="sponsor-group"><h3>Bronze</h3><span class="badge alt"></span><span class="badge"></span></div>
    <div class="sponsor-group"><h3>Media</h3><span class="badge"></span><span class="badge alt"></span></div>
    <div class="sponsor-group"><h3>Support</h3><span class="badge alt"></span><span class="badge"></span></div>
  </section>
</main>
</body>
</html>
```